Brantley Studios photography and video creator

I need a business card for my production company. I shoot photography and videography for real estate, adventure sports and businesses

Contact Information for Business Card

simple not to busy

Colors

Designer to choose colors to be used in the design.

Requirements
Must have
• derek@brantleystudios.ca
• phone -5873304127
• instagram derek_brantley

```html
<!DOCTYPE html>
<html lang="en">
<head>
<meta charset="utf-8">
<title>Brantley Studios – Business Card</title>
<link href="https://fonts.googleapis.com/css2?family=Montserrat:wght@400;500;600;700&display=swap" rel="stylesheet">
<style>
  :root {
    --page: #d9d9d9;
    --card-dark: #262626;
    --card-dark-edge: #1c1c1c;
    --paper: #ffffff;
    --band: #8c8c8c;
    --ring: #c4c4c4;
    --text-light: #f2f2f2;
    --text-soft: #dcdcdc;
    --scene-top: #e6e6e6;
    --scene-mid: #8f8f8f;
    --scene-low: #1a1a1a;
  }
  * { box-sizing: border-box; margin: 0; padding: 0; }
  html, body { width: 1200px; height: 930px; overflow: hidden; }
  body {
    background: var(--page);
    font-family: "Montserrat", sans-serif;
    position: relative;
  }
  .card {
    position: absolute;
    border-radius: 22px;
    overflow: hidden;
    background: var(--card-dark);
    box-shadow: 0 6px 18px rgba(0,0,0,0.25);
  }
  .card svg.card-art { position: absolute; inset: 0; }

  /* back side */
  .card-back { left: 90px; top: 80px; width: 540px; height: 308px; }
  .card-back .wordmark { position: absolute; left: 190px; top: 128px; width: 160px; text-align: center; }
  .card-back .wordmark span { font-size: 19px; }
  .card-back .wordmark small { font-size: 8px; letter-spacing: 3px; }

  /* front side */
  .card-front { left: 470px; top: 480px; width: 640px; height: 366px; }
  .wordmark {
    color: var(--paper);
    font-weight: 700;
    line-height: 1.05;
  }
  .wordmark span, .wordmark small { display: block; }
  .card-front .wordmark { position: absolute; left: 360px; top: 170px; width: 220px; text-align: center; }
  .card-front .wordmark span { font-size: 30px; }
  .card-front .wordmark small { font-size: 11px; letter-spacing: 5px; margin-top: 4px; }

  .address {
    position: absolute; left: 40px; top: 100px;
    color: var(--text-light);
    font-size: 15px; line-height: 22px; font-weight: 400;
  }
  .identity { position: absolute; left: 40px; top: 214px; color: var(--paper); }
  .identity .name { font-size: 24px; font-weight: 600; letter-spacing: 0.5px; text-transform: uppercase; line-height: 28px; }
  .identity .role { font-size: 15px; font-weight: 400; color: var(--text-soft); line-height: 20px; }

  .contacts {
    position: absolute; left: 40px; top: 290px;
    list-style: none;
    color: var(--text-light);
    font-size: 15px; line-height: 23px;
  }
  .contacts li { display: flex; align-items: center; gap: 8px; }
  .contacts svg { width: 12px; height: 12px; flex: none; }
</style>
</head>
<body>

  <section class="card card-back" aria-label="Card back">
    <svg class="card-art" width="540" height="308" viewBox="0 0 540 308">
      <defs>
        <linearGradient id="sceneBack" x1="0" y1="0" x2="0" y2="1">
          <stop offset="0" stop-color="var(--scene-top)"/>
          <stop offset="0.5" stop-color="var(--scene-mid)"/>
          <stop offset="1" stop-color="var(--scene-low)"/>
        </linearGradient>
      </defs>
      <circle cx="270" cy="150" r="78" fill="url(#sceneBack)" role="img" aria-label="Mountain and pine tree landscape"/>
    </svg>
    <div class="wordmark"><span>BRANTLEY</span><small>STUDIOS</small></div>
  </section>

  <section class="card card-front" aria-label="Card front">
    <svg class="card-art" width="640" height="366" viewBox="0 0 640 366">
      <defs>
        <linearGradient id="sceneFront" x1="0" y1="0" x2="0" y2="1">
          <stop offset="0" stop-color="var(--scene-top)"/>
          <stop offset="0.5" stop-color="var(--scene-mid)"/>
          <stop offset="1" stop-color="var(--scene-low)"/>
        </linearGradient>
      </defs>
      <rect class="name-band" x="0" y="208" width="380" height="64" fill="var(--band)"/>
      <rect x="470" y="0" width="170" height="366" fill="var(--paper)"/>
      <circle cx="470" cy="150" r="168" fill="var(--paper)"/>
      <circle cx="470" cy="150" r="142" fill="none" stroke="var(--ring)" stroke-width="2"/>
      <circle cx="470" cy="150" r="132" fill="url(#sceneFront)" role="img" aria-label="Mountain and pine tree landscape"/>
    </svg>

    <div class="wordmark"><span>BRANTLEY</span><small>STUDIOS</small></div>

    <p class="address">612 Halden Boulevard<br>Millbrook, PA 18204</p>

    <div class="identity">
      <p class="name">Jonah Reyes</p>
      <p class="role">Managing Director</p>
    </div>

    <ul class="contacts">
      <li>
        <svg viewBox="0 0 12 12" aria-hidden="true"><path d="M2.5 1 L4.5 1 L5 3.5 L3.8 4.4 Q4.8 6.8 7.6 8.2 L8.5 7 L11 7.5 L11 9.5 Q10.5 11 9 11 Q1 10 1 3 Q1 1.5 2.5 1Z" fill="var(--text-light)"/></svg>
        5873304127
      </li>
      <li>
        <svg viewBox="0 0 12 12" aria-hidden="true"><rect x="1" y="2.5" width="10" height="7" fill="none" stroke="var(--text-light)" stroke-width="1.2"/><path d="M1 2.5 L6 6.5 L11 2.5" fill="none" stroke="var(--text-light)" stroke-width="1.2"/></svg>
        derek@brantleystudios.ca
      </li>
      <li>
        <svg viewBox="0 0 12 12" aria-hidden="true"><rect x="1" y="1" width="10" height="10" rx="1" fill="var(--text-light)"/></svg>
        instagram derek_brantley
      </li>
    </ul>
  </section>

</body>
</html>
```